vTend Cookbook Cover

I need a design (front and back) for a cookbook cover. Our partners are looking for a few ideas to pick from.
You can see the style for one of the cookbooks we currently carry - uploaded with this brief.
This cookbook is a little different than most cookbooks out there. It is a cancer-fighting cookbook but we don't want it to be so cancer focused that people who don't have cancer will not buy. The book starts out with a section for Foods that Help, then goes to another section called Foods that Hurt. Then, we provide a Recipes section from the ingredients found in Foods that Help. Finally, the last section is called Beyond the Plate and deals with healthy lifestyle habits. You can see a rough draft of the content of the book at the link below. Please keep in mind that the current covers you see are not at all what we want. These were just put there to fill in the space.
Link for cookbook content: https://www.filecrate-share.net/s/4kq29lmzwpbtnxv/The%20Bright%20Bowl%20-%20EDITED.pdf?dl=0
The title: The Bright Bowl
Subtitle: Nourishing Health One Dish at a Time
Author: Mirel Ostvan
The company that puts the book out is vTend. It would be nice to have the logo somewhere small. Logo can be found here: https://www.filecrate-share.net/s/hrp61wetcozuv3m/vTend%20Logo%20%26%20Guidelines.zip?dl=0
Like "Hand Over A Warmer Day" attached to this brief, we do NOT want something somber but more on the bright side. Just make it look nice and fresh. It would also be nice to somehow incorporate the concept of the cancer ribbon or a silhouette of it in a way that is not upfront but can still be acknowledge. No need for it to be pink and if that does not work, than it's better just to leave it out.
For the back cover, you can design it but simply leave room for us to fill in some text. No need for a spine design as it will be spiral bound.
The file must be designed and saved in PHOTOSHOP format.
According to the designer, the dimensions are:
207mm x 270mm + 5mm bleed
If you want to use the recipe pictures somehow in the cover, just snatch a picture from the content PDF and we can always replace it with the original larger file at a later time. Unfortunately, I don't have the pictures uploaded in filecrate.

```html
<!DOCTYPE html>
<html lang="en">
<head>
<meta charset="utf-8">
<title>The Bright Bowl — Cookbook Cover</title>
<link href="https://fonts.googleapis.com/css2?family=PT+Sans:wght@700&family=Tinos:wght@700&display=swap" rel="stylesheet">
<style>
  :root {
    --backdrop: #bb8bbf;
    --photo-cream: #ece6d6;
    --photo-green: #9cc25a;
    --photo-orange: #f08a2a;
    --photo-tomato: #d8402e;
    --badge-red: #e4102f;
    --badge-magenta: #d1066c;
    --white: #ffffff;
    --ink: #161616;
    --logo-grey: #55595c;
    --logo-dot: #d52b2b;
  }
  * { margin: 0; padding: 0; box-sizing: border-box; }
  html, body {
    width: 1200px;
    height: 1200px;
    overflow: hidden;
    background: var(--backdrop);
  }
  .cover {
    position: absolute;
    left: 294px;
    top: 155px;
    width: 655px;
    height: 855px;
    overflow: hidden;
  }
  .cover-photo {
    position: absolute;
    inset: 0;
    background:
      linear-gradient(135deg, var(--photo-green) 0%, var(--photo-cream) 22%, var(--photo-cream) 45%, var(--photo-orange) 58%, var(--photo-cream) 72%, var(--photo-green) 88%, var(--photo-tomato) 100%);
    opacity: 0.85;
  }
  .title-badge {
    position: absolute;
    left: 106px;
    top: 178px;
    width: 464px;
    height: 464px;
  }
  .publisher-mark {
    position: absolute;
    right: 40px;
    top: 38px;
    display: flex;
    align-items: center;
    gap: 6px;
  }
  .publisher-dot {
    width: 10px;
    height: 10px;
    border-radius: 50%;
    background: var(--logo-dot);
  }
  .publisher-name {
    font-family: "PT Sans", sans-serif;
    font-weight: 700;
    font-size: 26px;
    color: var(--logo-grey);
  }
  .title {
    position: absolute;
    left: 0;
    width: 676px;
    top: 306px;
    text-align: center;
    font-family: "PT Sans", sans-serif;
    font-weight: 700;
    font-size: 64px;
    line-height: 58px;
    letter-spacing: 1px;
    color: var(--white);
    text-transform: uppercase;
  }
  .subtitle {
    position: absolute;
    left: 0;
    width: 676px;
    top: 500px;
    text-align: center;
    font-family: "Tinos", serif;
    font-weight: 700;
    font-size: 22px;
    line-height: 32px;
    color: var(--white);
    text-transform: uppercase;
  }
  .author {
    position: absolute;
    left: 0;
    width: 668px;
    top: 802px;
    text-align: center;
    font-family: "Tinos", serif;
    font-weight: 700;
    font-size: 17px;
    color: var(--ink);
    text-transform: uppercase;
  }
</style>
</head>
<body>
  <main class="cover">
    <div class="cover-photo" role="img" aria-label="Overhead photo of fresh vegetables on a pale wooden table: spinach leaves, tomatoes, orange and red peppers, cucumber slices and a bowl of creamy dip"></div>

    <div class="publisher-mark">
      <span class="publisher-dot"></span>
      <span class="publisher-name">vTend</span>
    </div>

    <svg class="title-badge" viewBox="0 0 464 464" aria-hidden="true">
      <defs>
        <linearGradient id="badgeFill" x1="0" y1="0" x2="1" y2="0.3">
          <stop offset="0" stop-color="var(--badge-red)"/>
          <stop offset="0.45" stop-color="var(--badge-red)"/>
          <stop offset="0.75" stop-color="var(--badge-magenta)"/>
          <stop offset="1" stop-color="var(--badge-magenta)"/>
        </linearGradient>
      </defs>
      <circle cx="232" cy="232" r="232" fill="url(#badgeFill)" opacity="0.93"/>
      <circle cx="232" cy="232" r="214" fill="none" stroke="var(--white)" stroke-width="1.5" stroke-dasharray="6 5"/>
    </svg>

    <h1 class="title">The<br>Bright<br>Bowl</h1>
    <p class="subtitle">Nourishing Health<br>One Dish at a Time</p>
    <p class="author">Mirel Ostvan</p>
  </main>
</body>
</html>
```